NEW! Sports Supplement label
Vital Kinetic Laboratories
Project: NEW! Sports Supplement label
NEW! Sports Supplement label - Sports
Creative Brief
Looking for a new packaging design for a new line of products. This needs to be a clean label that delivers a scientific or medical feel in 3 colors with 4 lines for product descriptor sublines. <p><p> For Example: <p> • Muscle Recovery Acceleration <p> • Nitric Oxide Production <p> • Maximum Muscle Mass <p> • Improved Energy &amp; Focus <p><p> Use the following elements for presentation: <p><p> Name: VK260Q <p><p> 120 Capsules Dietary Supplement <p><p> The products are geared to Sports Supplements, Fat burners, preworkout supplements, sport drinks. <p><p> The fonts for the Product name and VKL logo must be destinctive elements and pop that adds value by providing consumers with instantly recognizable cues to help with the purchase decision making process. Preferrably reversed out white or black. <p> <p> Please see the following sites as example product labels for creative thought. They also provide actual full labels for your review: <p><p> http://www.plorvex.com/product/index.jsp?productId=48573920 http://www.plorvex.com/product/index.jsp?productId=48619375 http://www.plorvex.com/product/index.jsp?productId=48926054 <p><p> The label should be clean, in that it provides a clear, attractive space, with key information (4 line product descriptor mentioned above) on the front display panel necessary for a consumer to make a quick purchase decision. <p> The label should communicate a concise but informative message designed to make the consumer feel comfortable with the product by providing consumers with instantly recognizable cues (symbols of quality) to help with the purchase decision making process.
Sports
Sports nutrition products target a mass audience of consumers who have grown up knowing an active lifestyle has positive, long-term implications for health, fitness, weight management and longevity.
Please provide label design with color codes and in standard file formats with element layers. 2.75 x 7.00 4 x 9.375

```html
<!DOCTYPE html>
<html lang="en">
<head>
<meta charset="utf-8">
<title>VK260Q Dietary Supplement Label</title>
<link rel="stylesheet" href="https://fonts.googleapis.com/css2?family=Roboto:wght@700;900&family=PT+Sans:wght@700&display=swap">
<style>
  :root {
    --ink: #0d0d0d;
    --red: #d0121b;
    --silver-light: #f4f4f4;
    --silver-mid: #d6d6d6;
    --silver-dark: #a9a9a9;
    --panel: #ffffff;
    --band: #111111;
  }
  html, body {
    margin: 0;
    padding: 0;
    width: 1200px;
    height: 929px;
    overflow: hidden;
    background: #ffffff;
  }
  .label {
    position: relative;
    width: 1200px;
    height: 929px;
    overflow: hidden;
    background:
      repeating-linear-gradient(90deg, rgba(255,255,255,0.25) 0 2px, rgba(0,0,0,0.03) 2px 5px),
      linear-gradient(115deg, var(--silver-mid) 0%, var(--silver-light) 30%, var(--silver-dark) 48%, var(--silver-light) 62%, var(--silver-mid) 100%);
  }
  .band-top {
    position: absolute;
    left: 0; top: 0;
    width: 1200px; height: 50px;
    background: linear-gradient(180deg, #9a9a9a 0%, #e8e8e8 45%, #2a2a2a 75%, var(--band) 100%);
  }
  .band-bottom {
    position: absolute;
    left: 0; bottom: 0;
    width: 1200px; height: 38px;
    background: linear-gradient(180deg, var(--band) 0%, #3a3a3a 60%, #9a9a9a 100%);
  }
  .brand {
    position: absolute;
    left: 152px; top: 76px;
    margin: 0;
    font-family: "Roboto", Arial, sans-serif;
    font-weight: 900;
    font-size: 86px;
    line-height: 1;
    color: var(--ink);
  }
  .brand-name {
    position: absolute;
    left: 156px; top: 162px;
    margin: 0;
    font-family: "Roboto", Arial, sans-serif;
    font-weight: 700;
    font-size: 26px;
    line-height: 1.2;
    color: var(--ink);
    letter-spacing: 0.3px;
  }
  .product-name {
    position: absolute;
    left: 150px; top: 250px;
    margin: 0;
    font-family: "Roboto", Arial, sans-serif;
    font-weight: 900;
    font-size: 236px;
    line-height: 1;
    color: var(--ink);
    white-space: nowrap;
  }
  .product-type {
    position: absolute;
    right: 150px; top: 459px;
    margin: 0;
    font-family: "Roboto", Arial, sans-serif;
    font-weight: 700;
    font-size: 60px;
    line-height: 1;
    color: var(--ink);
    white-space: nowrap;
  }
  .info-panel {
    position: absolute;
    left: 118px; top: 542px;
    width: 966px; height: 360px;
    background: var(--panel);
    border-radius: 24px 24px 0 0;
    box-shadow: 0 0 10px rgba(0,0,0,0.25);
  }
  .benefits {
    position: absolute;
    left: 38px; top: 67px;
    margin: 0; padding: 0;
    list-style: none;
    font-family: "PT Sans", Arial, sans-serif;
    font-weight: 700;
    font-size: 31px;
    line-height: 42px;
    color: var(--ink);
  }
  .benefits li {
    display: flex;
    align-items: center;
    gap: 18px;
    white-space: nowrap;
  }
  .benefits svg { flex: none; }
  .count-badge {
    position: absolute;
    left: 879px; top: 745px;
    width: 168px; height: 146px;
    background: var(--ink);
    border-radius: 22px 22px 0 0;
    color: #fff;
    text-align: center;
    font-family: "Roboto", Arial, sans-serif;
    font-weight: 900;
  }
  .count-number {
    display: block;
    font-size: 92px;
    line-height: 1;
    margin-top: 12px;
  }
  .count-unit {
    display: block;
    font-size: 24px;
    line-height: 1;
    letter-spacing: 0.5px;
    margin-top: 6px;
  }
</style>
</head>
<body>
<main class="label">
  <div class="band-top"></div>

  <p class="brand">VKL</p>
  <p class="brand-name">VITAL KINETIC LABORATORIES</p>

  <h1 class="product-name">VK260Q</h1>
  <p class="product-type">DIETARY SUPPLEMENT</p>

  <section class="info-panel">
    <ul class="benefits">
      <li><svg width="16" height="20" viewBox="0 0 16 20"><path d="M2 2 L13 10 L2 18 L5 10 Z" fill="#d0121b"/></svg>Muscle Recovery Acceleration</li>
      <li><svg width="16" height="20" viewBox="0 0 16 20"><path d="M2 2 L13 10 L2 18 L5 10 Z" fill="#d0121b"/></svg>NItric Oxide Production</li>
      <li><svg width="16" height="20" viewBox="0 0 16 20"><path d="M2 2 L13 10 L2 18 L5 10 Z" fill="#d0121b"/></svg>Maximum Musle Mass</li>
      <li><svg width="16" height="20" viewBox="0 0 16 20"><path d="M2 2 L13 10 L2 18 L5 10 Z" fill="#d0121b"/></svg>Improved Energy &amp; Focus</li>
    </ul>
  </section>

  <div class="count-badge">
    <span class="count-number">30</span>
    <span class="count-unit">CAPSULES</span>
  </div>

  <div class="band-bottom"></div>
</main>
</body>
</html>
```